Homepage Website Design for luxury picnic company

We need a homepage designed for a luxury picnic business to match our updated branding/logo which we're currently completing on ArtGatherly with another competition. Please see attached logo/colour example to use for now.

PLEASE NOTE: We are only after graphic design concepts as part of this competition. I will get another developer to actually code the website.

It is important that this website is very elegant/luxurious and stands out from a visual perspective. The images really need to match the content/sections also. The new branding colours are silver with a dark background. Please create the new website homepage to match these colours/branding.

Please create as many concepts as possible and then I will provide feedback from there

The website content including sections is here https://pages.velmoranote.com/doc/d/7kRtWq2mLp9XcVb4Hn8Js3Yd6Fg1Za5Qe0Uo2Ti/edit?mode=share

Images to use are located here https://vault.trenquilbox.com/vault/dirs/5HmQzR2-NcWy8Kp41-7VbLdTsXoeFj?mode=share and there is also lots of videos at this link which you can screenshot images out of if needed https://www.stashquarry.com/sh/k827trwm3hdz4/AACvnRt2Lm8WqPe5Xu9JdsYk?dl=0

Any questions please contact me

```html
<!DOCTYPE html>
<html lang="en">
<head>
<meta charset="utf-8">
<title>Ridgeline Picnics – Luxury Picnics</title>
<link href="https://fonts.googleapis.com/css2?family=Lato:wght@300;400;700;900&family=Montserrat:wght@400;600;700&display=swap" rel="stylesheet">
<style>
:root{
  --navy:#131a34;
  --navy-deep:#0d1229;
  --ink:#222;
  --muted:#666;
  --line:#cfcfcf;
  --white:#fff;
  --gold:#f2be1a;
}
*{box-sizing:border-box;margin:0;padding:0}
html,body{width:1200px;height:5386px;overflow:hidden}
body{position:relative;font-family:"Lato",sans-serif;color:var(--ink);background:var(--white)}
.abs{position:absolute}
.photo{position:absolute;display:block}

/* header */
.brand{position:absolute;left:112px;top:34px;width:130px;height:70px;display:flex;align-items:center;gap:8px}
.brand-dot{width:14px;height:14px;border-radius:50%;background:var(--navy)}
.brand-name{font-family:"Lato",sans-serif;font-weight:700;font-size:19px;line-height:1.1;color:var(--navy)}
.menu-toggle{position:absolute;left:1003px;top:48px;font-size:16px;color:var(--navy);display:flex;align-items:center;gap:10px}
.menu-toggle i{display:block;width:28px;height:2px;background:var(--navy);box-shadow:0 5px 0 var(--navy),0 10px 0 var(--navy)}

/* hero */
.hero{position:absolute;left:0;top:0;width:1200px;height:637px;background:linear-gradient(180deg,#fff 0,#fff 70px,#cfd3d8 120px,#7b8490 220px,#5b5542 380px,#2f2a22 520px,#1f1c1a 637px)}
.hero-title{position:absolute;left:0;width:1200px;top:385px;text-align:center;color:#fff;font-weight:400;font-size:33px;letter-spacing:2px}
.hero-sub{position:absolute;left:0;width:1200px;top:428px;text-align:center;color:#fff;font-weight:400;font-size:25px;letter-spacing:1px}
.btn{position:absolute;display:flex;align-items:center;justify-content:center;background:var(--navy);color:#fff;font-family:"Montserrat",sans-serif;font-weight:700;font-size:14px}
.hero-dots{position:absolute;top:565px;left:582px;display:flex;gap:8px}
.hero-dots span{width:6px;height:6px;border-radius:50%;background:#fff;opacity:.7}
.hero-dots span.on{opacity:1;box-shadow:0 0 0 2px rgba(255,255,255,.4)}

.side-nav{position:absolute;left:111px;top:142px;width:125px;height:460px;background:#fff;display:flex;flex-direction:column;align-items:center;padding-top:30px;gap:22px;box-shadow:0 2px 10px rgba(0,0,0,.2)}
.side-nav a{display:flex;flex-direction:column;align-items:center;gap:6px;font-size:13px;color:var(--ink);text-decoration:none}
.side-nav a.active{font-weight:700}
.side-nav svg{width:18px;height:18px;fill:var(--navy)}

/* booking */
.booking{position:absolute;left:111px;top:606px;width:976px;height:138px;background:var(--navy-deep)}
.booking-inner{position:absolute;left:35px;top:31px;width:905px;height:74px;background:#fff;display:flex;align-items:center;padding:0 12px 0 21px;gap:13px}
.field{width:161px;height:40px;border:1px solid var(--line);display:flex;align-items:center;justify-content:space-between;padding:0 20px;font-size:13px;color:var(--ink)}
.field .caret{width:0;height:0;border-left:5px solid transparent;border-right:5px solid transparent;border-top:7px solid var(--ink)}
.booking .book{position:relative;width:188px;height:40px}

/* features */
.feature{position:absolute;top:815px;width:299px;height:485px;background:#fff;box-shadow:0 2px 8px rgba(0,0,0,.12)}
.feature .photo{left:0;top:0;width:299px;height:255px}
.feature h3{position:absolute;top:255px;left:0;width:299px;height:52px;background:var(--navy);color:#fff;font-weight:400;font-size:21px;letter-spacing:1px;display:flex;align-items:center;justify-content:center}
.feature p{position:absolute;top:325px;left:24px;width:251px;text-align:center;font-size:12px;line-height:20px;color:var(--muted)}

/* video */
.video{position:absolute;left:0;top:1358px;width:1200px;height:527px;background:linear-gradient(160deg,#3a4150 0%,#2b3038 40%,#3a342e 75%,#1f2226 100%)}
.play{position:absolute;left:563px;top:1571px;width:73px;height:73px;border:3px solid var(--gold);border-radius:50%}
.play::after{content:"";position:absolute;left:27px;top:20px;border-top:15px solid transparent;border-bottom:15px solid transparent;border-left:24px solid #fff}
.watch{position:absolute;left:657px;top:1585px;font-size:37px;letter-spacing:5px;color:#fff;font-weight:700}
.watch span{font-weight:300}

/* pricing */
.plan{position:absolute;color:#fff;overflow:hidden}
.plan .shade{position:absolute;inset:0;background:linear-gradient(180deg,rgba(19,26,52,.05) 0%,rgba(19,26,52,.85) 100%)}
.plan .copy{position:absolute;left:30px;right:30px}
.plan h4{font-family:"Montserrat",sans-serif;font-weight:600;font-size:15px;letter-spacing:1px;margin-bottom:8px}
.plan p{font-size:12px;line-height:20px;letter-spacing:.5px}
.plan .book-link{font-family:"Montserrat",sans-serif;font-weight:700;font-size:14px;letter-spacing:2px;margin-top:10px}

/* food */
.food{position:absolute;left:0;top:2533px;width:1200px;height:696px;background:linear-gradient(90deg,#ececec 0%,#e4e4e4 60%,#d9d9d9 100%)}
.frame{position:absolute;border:2px solid var(--navy)}
.section-title{position:absolute;font-size:33px;color:var(--ink);font-weight:700;letter-spacing:1px}
.section-title span{font-weight:300}
.food-copy{position:absolute;left:523px;width:560px;font-size:11.5px;line-height:21px;color:var(--muted)}
.food-list{position:absolute;left:523px;top:2884px;list-style:none}
.food-list li{position:relative;height:38px;padding-left:25px;font-weight:700;font-size:15px;color:#555}
.food-list li::before{content:"";position:absolute;left:0;top:4px;width:13px;height:13px;border-radius:50%;background:var(--navy)}

/* spots */
.center-title{position:absolute;left:0;width:1200px;text-align:center}
.spot{position:absolute;top:3386px;width:310px;height:297px;background:#fff;box-shadow:0 2px 8px rgba(0,0,0,.12)}
.spot .photo{left:0;top:0;width:310px;height:198px}
.spot h5{position:absolute;top:218px;width:100%;text-align:center;font-weight:400;font-size:18px;color:var(--ink)}
.spot a{position:absolute;top:252px;width:100%;text-align:center;font-weight:700;font-size:15px;color:var(--navy);text-decoration:underline}
.note{position:absolute;left:788px;top:3386px;width:299px;height:297px;background:#fff;box-shadow:0 2px 8px rgba(0,0,0,.12);padding:40px 30px}
.note h5{font-weight:700;font-size:25px;letter-spacing:1px;color:var(--ink);margin-bottom:14px}
.note p{font-size:14px;line-height:25px;color:#444}

/* testimonials */
.clients{position:absolute;left:0;top:3756px;width:1200px;height:497px;background:linear-gradient(90deg,#f1f1f1 0%,#e0e0e0 60%,#c9c9c9 100%)}
.quote{position:absolute;top:3900px;width:234px;height:270px;background:#fff;box-shadow:0 2px 8px rgba(0,0,0,.12);padding:70px 16px 0}
.quote p{font-size:12px;line-height:18px;color:var(--muted)}
.stars{display:flex;gap:2px;margin:8px 0 14px}
.stars svg{width:22px;height:22px;fill:var(--gold)}
.quote hr{border:0;border-top:1px solid var(--line);margin-bottom:18px}
.person{display:flex;align-items:center;gap:10px;font-size:15px;color:#333;font-variant:small-caps}
.avatar{width:42px;height:42px;border-radius:50%;background:linear-gradient(135deg,#8a8f99,#3b4150)}

/* strip + follow */
.strip{position:absolute;top:4253px;height:226px;width:241px}
.follow{position:absolute;left:533px;top:4412px;width:134px;height:134px;border-radius:50%;background:#fff;box-shadow:0 2px 10px rgba(0,0,0,.2);display:flex;flex-direction:column;align-items:center;justify-content:center;gap:10px;font-size:13px;font-weight:700;color:var(--ink)}
.follow i{width:30px;height:30px;border-radius:7px;background:#d6456f}

/* contact */
.contact-left{position:absolute;left:0;top:4479px;width:600px;height:447px;background:#fff}
.contact-right{position:absolute;left:600px;top:4479px;width:600px;height:447px;background:var(--navy)}
.contact-title{position:absolute;left:94px;top:4548px;font-size:33px;line-height:44px;color:var(--ink);font-weight:700}
.contact-title span{font-weight:300}
.contact-intro{position:absolute;left:94px;top:4648px;width:380px;font-size:13px;line-height:22px;color:var(--muted)}
.contact-row{position:absolute;left:94px;display:flex;align-items:center;gap:18px;font-weight:700;font-size:14px;color:var(--ink)}
.contact-row svg{width:22px;height:22px;fill:none;stroke:#555;stroke-width:1.6}
.form-label{position:absolute;left:681px;font-size:12px;color:#fff}
.form-line{position:absolute;left:681px;width:427px;height:1px;background:rgba(255,255,255,.5)}
.send{position:absolute;left:681px;top:4829px;display:flex;align-items:center;gap:12px;color:#fff;font-weight:700;font-size:17px;letter-spacing:1px}

/* footer */
.footer{position:absolute;left:0;top:4926px;width:1200px;height:460px;background:var(--navy-deep)}
.footer-brand{position:absolute;left:0;width:1200px;top:5038px;display:flex;justify-content:center;align-items:center;gap:10px}
.footer-brand .brand-name{color:#fff;font-size:30px}
.footer-brand .brand-dot{background:#fff;width:18px;height:18px}
.footer-text{position:absolute;left:220px;width:760px;top:5145px;text-align:center;font-size:12px;line-height:20px;color:#e3e3e3}
.social{position:absolute;left:530px;top:5246px;display:flex;gap:6px}
.social span{width:40px;height:40px;border:2px solid #fff;border-radius:50%}
.copyright{position:absolute;left:0;width:1200px;top:5322px;text-align:center;font-size:12px;color:#e3e3e3}
</style>
</head>
<body>

<section class="hero" role="img" aria-label="Couple sharing wine at a picnic overlooking a misty mountain valley"></section>

<header>
  <div class="brand"><span class="brand-dot"></span><span class="brand-name">Ridgeline<br>Picnics</span></div>
  <div class="menu-toggle">Menu <i></i></div>
</header>

<nav class="side-nav">
  <a class="active"><svg viewBox="0 0 20 20"><path d="M10 2 1 10h3v8h5v-5h2v5h5v-8h3z"/></svg>Home</a>
  <a><svg viewBox="0 0 20 20"><path d="M4 2h12v16H4zM6 4v12h8V4zm4 2a2 2 0 1 1 0 4 2 2 0 0 1 0-4zm-3 8c0-2 6-2 6 0z"/></svg>About</a>
  <a><svg viewBox="0 0 20 20"><path d="M2 5h16v11H2zm2 2v2h12V7zm0 5v2h5v-2z"/></svg>Pricing</a>
  <a><svg viewBox="0 0 20 20"><path d="M10 1a9 9 0 1 1 0 18 9 9 0 0 1 0-18zm0 4a5 5 0 1 0 0 10 5 5 0 0 0 0-10z"/></svg>Who We Are</a>
  <a><svg viewBox="0 0 20 20"><path d="M10 1a6 6 0 0 1 6 6c0 5-6 11-6 11S4 12 4 7a6 6 0 0 1 6-6zm0 3a3 3 0 1 0 0 6 3 3 0 0 0 0-6z"/></svg>Spot</a>
  <a><svg viewBox="0 0 20 20"><path d="M3 2h14v16H3zm7 3a3 3 0 1 0 0 6 3 3 0 0 0 0-6zm-5 11h10c0-4-10-4-10 0z"/></svg>Contact Us</a>
</nav>

<h1 class="hero-title">SHARE AN UNFORGETTABLE MOMENT</h1>
<p class="hero-sub">Luxury picnics at breathtaking locations</p>
<a class="btn" style="left:510px;top:472px;width:180px;height:38px">Book Your Picnic</a>
<div class="hero-dots"><span></span><span class="on"></span><span></span></div>

<section class="booking">
  <form class="booking-inner">
    <div class="field">Arrival Date <svg width="18" height="16" viewBox="0 0 18 16"><rect x="1" y="2" width="16" height="13" fill="none" stroke="#555" stroke-width="1.5"/><path d="M1 6h16M5 0v4M13 0v4" stroke="#555" stroke-width="1.5"/></svg></div>
    <div class="field">Select Place <svg width="18" height="18" viewBox="0 0 18 18"><circle cx="9" cy="9" r="6" fill="none" stroke="#555" stroke-width="1.5"/><circle cx="9" cy="9" r="2" fill="#555"/><path d="M9 0v4M9 14v4M0 9h4M14 9h4" stroke="#555" stroke-width="1.5"/></svg></div>
    <div class="field">Adults <span class="caret"></span></div>
    <div class="field">Children <span class="caret"></span></div>
    <a class="btn book">Book Your Picnic</a>
  </form>
</section>

<article class="feature" style="left:111px">
  <div class="photo" role="img" aria-label="Champagne on ice beside a grazing platter" style="background:linear-gradient(180deg,#9aa0a8,#6b5a50 60%,#5a2a26)"></div>
  <h3>BLISS</h3>
  <p>We enable you to enjoy true quality time with your partner, friends or family. We do this by creating the perfect atmosphere to celebrate a special moment in your life or to simply spoil yourself!</p>
</article>
<article class="feature" style="left:449px">
  <div class="photo" role="img" aria-label="Couple embracing above a mountain valley" style="background:linear-gradient(180deg,#8f9aa8,#5d6670 55%,#3a3430)"></div>
  <h3>UNWIND</h3>
  <p>Let us do everything for you so you can enjoy a stress free experience. You will also discover the Ridgeline Ranges like you never have before! Each of our picnic spots are absolutely stunning and also very private.</p>
</article>
<article class="feature" style="left:788px">
  <div class="photo" role="img" aria-label="Close-up of cheese, strawberries and grapes" style="background:linear-gradient(135deg,#5a1a22,#8c2a30 50%,#d9d2c2)"></div>
  <h3>INDULGE</h3>
  <p>Our delicious picnics will have your mouth watering! You can design your own picnic by choosing from our extensive menu along with 2 choices of your favourite alcoholic &amp; non-alcoholic beverages. We cater for all dietary requirements and also have a BYO option.</p>
</article>

<section class="video" role="img" aria-label="Couple relaxing on cushions at a cliff-top picnic at dusk"></section>
<div class="play"></div>
<div class="watch">WATCH <span>VIDEO</span></div>

<article class="plan" style="left:111px;top:1958px;width:485px;height:450px;background:linear-gradient(180deg,#8ea3bd,#c7ccd2 40%,#4e5565 70%,#1f2640)" role="img" aria-label="Clouds over a mountain lookout">
  <div class="shade"></div>
  <div class="copy" style="top:250px">
    <h4>BYO PICNIC - $200 + GST</h4>
    <p>Hire, transport and setup of picnic equipment, directions to 'secret' location. 2 hour picnic, cleaning and pack up, still or sparkling water cooled on ice with glassware. BYO additional food &amp; beverages</p>
    <p class="book-link">(Book Now)</p>
  </div>
</article>
<article class="plan" style="left:604px;top:1958px;width:483px;height:220px;background:linear-gradient(180deg,#5b6678,#2a3248)" role="img" aria-label="Picnic setting on a cliff edge">
  <div class="shade"></div>
  <div class="copy" style="top:62px">
    <h4 style="font-size:14px;margin-bottom:2px">Gourmet Picnic - $350 + GST</h4>
    <p style="font-size:11.5px;line-height:21px;letter-spacing:0">Everything in the BYO picnic, design your own gourmet grazing platter, choose 2 types of complimentary beverages, delivery of the food and beverages to the picnic spot, matching glassware and cutlery</p>
    <p class="book-link" style="margin-top:2px">(Book Now)</p>
  </div>
</article>
<article class="plan" style="left:604px;top:2186px;width:483px;height:222px;background:linear-gradient(180deg,#6a7080,#2a3048)" role="img" aria-label="Kangaroo in misty bushland">
  <div class="shade"></div>
  <div class="copy" style="top:64px">
    <h4 style="font-size:14px;margin-bottom:2px">Proposal Picnic - $100 + GST</h4>
    <p style="font-size:11.5px;line-height:21px;letter-spacing:0">1 on 1 VIP treatment, suggestions for accommodation, activities, restaurants, assistance with any requests, directions to location prior to the picnic, help with organising photography, anything else needed for a successful proposal</p>
    <p class="book-link" style="margin-top:2px">(Book Now)</p>
  </div>
</article>
<a class="btn" style="left:453px;top:2429px;width:293px;height:37px">View Our All Payment Plans</a>

<section class="food"></section>
<div class="frame" style="left:64px;top:2602px;width:200px;height:199px"></div>
<div class="photo" role="img" aria-label="Grazing board with drinks on ice" style="left:52px;top:2613px;width:199px;height:188px;background:linear-gradient(180deg,#9aa3ad,#6b5a50 55%,#5c2626)"></div>
<div class="frame" style="left:160px;top:2671px;width:300px;height:412px"></div>
<div class="photo" role="img" aria-label="Bottles of wine and craft beer in the bush" style="left:146px;top:2681px;width:303px;height:412px;background:linear-gradient(180deg,#5a7048,#3a4a30 40%,#6a2a24 75%,#c0a080)"></div>
<div class="frame" style="left:12px;top:2947px;width:240px;height:198px"></div>
<div class="photo" role="img" aria-label="Cheese and fruit platter on a red rug" style="left:0;top:2957px;width:251px;height:188px;background:linear-gradient(135deg,#6a1e22,#9a3a30 55%,#c8b090)"></div>

<h2 class="section-title" style="left:518px;top:2604px">FOOD <span>&amp; BEVERAGES</span></h2>
<p class="food-copy" style="top:2652px">Our delicious food and beverages will have your mouth watering regardless of your tastes or dietary requirements. Our Gourmet Picnic menu is fully customisable so you can design your own picnic. We cater for allergies, vegans, coeliacs and all other dietary requirements. It is quick and easy to select your choices via our website which means it is no big deal if you do have specific requirements!</p>
<p class="food-copy" style="top:2768px">We focus on offering a lot of diversity with the finest ingredients. We're a registered food business meaning we prepare, store and transport our food in accordance with all food handling guidelines. We have also put a lot of thought into the logistics of serving this food at our picnic locations and ensure the food is as refrigerated and fresh as possible. Each Gourmet Picnic includes the following</p>
<ul class="food-list">
  <li>2 choices of cheese, dips or antipasto</li>
  <li>2 choices of crackers</li>
  <li>Seasonal fruit</li>
  <li>1 choice of nuts or dried fruit</li>
  <li>1 choice of chocolate</li>
  <li>2 choices of complimentary beer, wine or non-alcoholic beverages</li>
</ul>
<a class="btn" style="left:525px;top:3118px;width:148px;height:36px">View Menu</a>

<h2 class="center-title section-title" style="top:3282px">OUR PICNIC <span>SPOTS</span></h2>
<p class="center-title" style="top:3332px;font-size:11.5px;line-height:21px;color:var(--muted)">You will love our breathtaking locations which you can't find on Findly! The only way to experience<br>these stunning spots first hand is by organising a picnic with us.</p>

<article class="spot" style="left:111px">
  <div class="photo" role="img" aria-label="Picnic group on a rocky ledge above the valley" style="background:linear-gradient(180deg,#7a8595,#4a5260 50%,#5a4438)"></div>
  <h5>Cascade Falls Picnic Spot</h5>
  <a>View Available Dares &amp; Times</a>
</article>
<article class="spot" style="left:445px">
  <div class="photo" role="img" aria-label="Lantern and picnic setup overlooking a wide valley" style="background:linear-gradient(180deg,#a8b2be,#6a7280 50%,#3e3a36)"></div>
  <h5>Summit Rock Picnic Spot</h5>
  <a>View Available Dares &amp; Times</a>
</article>
<aside class="note">
  <h5>IMPORTANT NOTE</h5>
  <p>We don't publicly advertise our exact locations so we can continue to keep them a secret. For this reason we provide our clients with the directions the day prior to the picnic and ask that you do not share the exact location!</p>
</aside>

<section class="clients" role="img" aria-label="Faded mountain landscape behind client reviews"></section>
<h2 class="center-title section-title" style="top:3832px;font-weight:400">WHAT OUR CLIENTS <span>ARE SAYING...</span></h2>

<article class="quote" style="left:92px">
  <p>It is a long established fact that a reader will be distracted by the readable content of a page when looking.</p>
  <div class="stars"><svg viewBox="0 0 24 24"><path d="M12 2l3 7h7l-5.5 4.5 2 7.5-6.5-4.5L5.5 21l2-7.5L2 9h7z"/></svg><svg viewBox="0 0 24 24"><path d="M12 2l3 7h7l-5.5 4.5 2 7.5-6.5-4.5L5.5 21l2-7.5L2 9h7z"/></svg><svg viewBox="0 0 24 24"><path d="M12 2l3 7h7l-5.5 4.5 2 7.5-6.5-4.5L5.5 21l2-7.5L2 9h7z"/></svg><svg viewBox="0 0 24 24"><path d="M12 2l3 7h7l-5.5 4.5 2 7.5-6.5-4.5L5.5 21l2-7.5L2 9h7z"/></svg><svg viewBox="0 0 24 24"><path d="M12 2l3 7h7l-5.5 4.5 2 7.5-6.5-4.5L5.5 21l2-7.5L2 9h7z"/></svg></div>
  <hr><div class="person"><span class="avatar" role="img" aria-label="Client portrait"></span>Tom N.</div>
</article>
<article class="quote" style="left:355px">
  <p>It is a long established fact that a reader will be distracted by the readable content of a page when looking.</p>
  <div class="stars"><svg viewBox="0 0 24 24"><path d="M12 2l3 7h7l-5.5 4.5 2 7.5-6.5-4.5L5.5 21l2-7.5L2 9h7z"/></svg><svg viewBox="0 0 24 24"><path d="M12 2l3 7h7l-5.5 4.5 2 7.5-6.5-4.5L5.5 21l2-7.5L2 9h7z"/></svg><svg viewBox="0 0 24 24"><path d="M12 2l3 7h7l-5.5 4.5 2 7.5-6.5-4.5L5.5 21l2-7.5L2 9h7z"/></svg><svg viewBox="0 0 24 24"><path d="M12 2l3 7h7l-5.5 4.5 2 7.5-6.5-4.5L5.5 21l2-7.5L2 9h7z"/></svg><svg viewBox="0 0 24 24"><path d="M12 2l3 7h7l-5.5 4.5 2 7.5-6.5-4.5L5.5 21l2-7.5L2 9h7z"/></svg></div>
  <hr><div class="person"><span class="avatar" role="img" aria-label="Client portrait"></span>Alan C.</div>
</article>
<article class="quote" style="left:617px">
  <p>It is a long established fact that a reader will be distracted by the readable content of a page when looking.</p>
  <div class="stars"><svg viewBox="0 0 24 24"><path d="M12 2l3 7h7l-5.5 4.5 2 7.5-6.5-4.5L5.5 21l2-7.5L2 9h7z"/></svg><svg viewBox="0 0 24 24"><path d="M12 2l3 7h7l-5.5 4.5 2 7.5-6.5-4.5L5.5 21l2-7.5L2 9h7z"/></svg><svg viewBox="0 0 24 24"><path d="M12 2l3 7h7l-5.5 4.5 2 7.5-6.5-4.5L5.5 21l2-7.5L2 9h7z"/></svg><svg viewBox="0 0 24 24"><path d="M12 2l3 7h7l-5.5 4.5 2 7.5-6.5-4.5L5.5 21l2-7.5L2 9h7z"/></svg><svg viewBox="0 0 24 24"><path d="M12 2l3 7h7l-5.5 4.5 2 7.5-6.5-4.5L5.5 21l2-7.5L2 9h7z"/></svg></div>
  <hr><div class="person"><span class="avatar" role="img" aria-label="Client portrait"></span>Erin W.</div>
</article>
<article class="quote" style="left:872px">
  <p>It is a long established fact that a reader will be distracted by the readable content of a page when looking.</p>
  <div class="stars"><svg viewBox="0 0 24 24"><path d="M12 2l3 7h7l-5.5 4.5 2 7.5-6.5-4.5L5.5 21l2-7.5L2 9h7z"/></svg><svg viewBox="0 0 24 24"><path d="M12 2l3 7h7l-5.5 4.5 2 7.5-6.5-4.5L5.5 21l2-7.5L2 9h7z"/></svg><svg viewBox="0 0 24 24"><path d="M12 2l3 7h7l-5.5 4.5 2 7.5-6.5-4.5L5.5 21l2-7.5L2 9h7z"/></svg><svg viewBox="0 0 24 24"><path d="M12 2l3 7h7l-5.5 4.5 2 7.5-6.5-4.5L5.5 21l2-7.5L2 9h7z"/></svg><svg viewBox="0 0 24 24"><path d="M12 2l3 7h7l-5.5 4.5 2 7.5-6.5-4.5L5.5 21l2-7.5L2 9h7z"/></svg></div>
  <hr><div class="person"><span class="avatar" role="img" aria-label="Client portrait"></span>Gary D.</div>
</article>

<div class="photo strip" style="left:0;background:linear-gradient(180deg,#5a6a80,#2f3a4a)" role="img" aria-label="Valley lookout at dusk"></div>
<div class="photo strip" style="left:240px;background:linear-gradient(180deg,#c8a888,#7a2a2a)" role="img" aria-label="Couple toasting at a picnic"></div>
<div class="photo strip" style="left:480px;background:linear-gradient(180deg,#8a7058,#3a2a24)" role="img" aria-label="Lantern on a picnic rug"></div>
<div class="photo strip" style="left:720px;background:linear-gradient(180deg,#6a7a58,#5a2a24)" role="img" aria-label="Wine bottles on a picnic table"></div>
<div class="photo strip" style="left:960px;background:linear-gradient(180deg,#7a8a98,#4a4a40)" role="img" aria-label="Guests walking through bushland"></div>
<div class="follow">Follow Us On<i></i></div>

<section class="contact-left"></section>
<section class="contact-right"></section>
<h2 class="contact-title">STAY IN TOUCH <span>AND TELL<br>US YOUR EXPERIENCE</span></h2>
<p class="contact-intro">View the Help Desk or send an email to support if you have any questions at all.</p>
<div class="abs" style="left:94px;top:4703px;width:380px;height:1px;background:var(--line)"></div>
<div class="contact-row" style="top:4729px"><svg viewBox="0 0 24 24"><rect x="3" y="5" width="18" height="14"/><path d="M6 9h6M6 13h4M15 9h3v4h-3z"/></svg>PO Box 1180 FERNVALE RIDGE 2799</div>
<div class="contact-row" style="top:4792px"><svg viewBox="0 0 24 24"><path d="M3 9c0-3 4-4 9-4s9 1 9 4l-3 2-2-2H8l-2 2zM6 12h12l2 7H4z"/></svg>02 5550 1234</div>
<div class="contact-row" style="top:4855px"><svg viewBox="0 0 24 24"><path d="M5 3l4 1 1 4-2 2a11 11 0 0 0 6 6l2-2 4 1 1 4-3 2C10 20 4 14 3 6z"/></svg>info@ridgelinepicnics.com.au</div>

<div class="form-label" style="top:4559px">Full Name</div><div class="form-line" style="top:4598px"></div>
<div class="form-label" style="top:4636px">Email Address</div><div class="form-line" style="top:4675px"></div>
<div class="form-label" style="top:4713px">Message</div><div class="form-line" style="top:4790px"></div>
<div class="send">SEND <svg width="30" height="10" viewBox="0 0 30 10"><path d="M0 5h27M23 1l4 4-4 4" stroke="#fff" stroke-width="1.6" fill="none"/></svg></div>

<footer class="footer"></footer>
<div class="footer-brand"><span class="brand-dot"></span><span class="brand-name">Ridgeline Picnics</span></div>
<p class="footer-text">We are very conscious of everyone's health and well being during these unprecedented times. You can have confidence knowing we're a registered COVID safe business with the State Health Authority. We follow all health protocols when setting up and preparing our picnics. If you want to know any further details or have any requests please just reach out.</p>
<div class="social"><span></span><span></span><span></span></div>
<p class="copyright">Copyright © 2020 RIDGELINE PICNICS &nbsp;|&nbsp; All Rights Reserved</p>

</body>
</html>
```